MallNova Brochure/Booklet Design

I am seeking a luxury finish booklet with the attached content. The same pictures can be used or different ones. It needs to be classy, but EDGY

This new company targets the owners of shopping centres and provides a number of services including marketing/community involvement/digital technology/social media etc. I'd love to see the use of our logo colours and a way to make this really pop!

I'm looking to develop a relationship with a designer that we can work on many more projects with.

I'm not interested in seeing any SAMPLES, only designs that use the brief (our content, logo, colours and font).
Updates

Please do not submit SAMPLES of your other work, we are only interested in seeing designs that work to our brief (content, logo, colour and font)

Reason: There has not been any designs submitted that are of a high enough standard. I'd like to see more use of the colours as backgrounds rather than plain white and some more interesting ideas. Please do not submit samples of your other works.

for brochure inspiration check out the following links... i think bright/classy

Target Market(s)

corporate but with a wow, not standard - this is something millionaires and billionaires will be presented with and they will only look at it for 5 mins so it needs to grab them!

http://www.plimvoro.example/blog/handpicked-printed-brochures/

http://quarneltrove.example/articles/30-best-brochure-designs-for-your-inspiration/

http://www.zivendale.example/2012/04/26/40-unique-and-beautiful-examples-of-brochure-design/

Industry/Entity Type

Shopping

Font styles to use
Other font styles liked:
• ubuntu

Requirements
Must have
• Must have the content supplied included and our logo used
Must use UBUNTU font
Should not have
• Should not be a sample, must abide by the brief

```html
<!DOCTYPE html>
<html lang="en">
<head>
<meta charset="utf-8">
<title>MallNova Brochure Cover</title>
<link rel="stylesheet" href="https://fonts.googleapis.com/css2?family=Ubuntu:wght@400;500;700&display=swap">
<style>
  :root {
    --stage: #e4e5e7;
    --navy-deep: #0a2e55;
    --navy: #0f4277;
    --blue-mid: #16609c;
    --cyan-glow: #21b0e6;
    --word-light: #a9daf2;
    --word-dim: rgba(150, 200, 230, 0.45);
    --white: #ffffff;
  }
  * { box-sizing: border-box; margin: 0; padding: 0; }
  html, body { width: 1200px; height: 835px; overflow: hidden; }
  body {
    background: var(--stage);
    font-family: "Ubuntu", sans-serif;
    position: relative;
  }
  .brochure {
    position: absolute;
    left: 105px; top: 67px;
    width: 990px; height: 700px;
    display: flex;
    box-shadow: 0 12px 30px rgba(0,0,0,0.25);
  }
  .panel {
    position: relative;
    width: 495px; height: 700px;
    overflow: hidden;
    background:
      radial-gradient(ellipse 380px 260px at 60% 78%, rgba(33,176,230,0.55), transparent 70%),
      linear-gradient(180deg, var(--navy-deep) 0%, var(--navy) 55%, var(--blue-mid) 80%, var(--navy) 100%);
  }
  .panel--back {
    background:
      radial-gradient(ellipse 300px 240px at 100% 70%, rgba(33,176,230,0.45), transparent 70%),
      linear-gradient(180deg, var(--navy-deep) 0%, var(--navy) 60%, var(--navy-deep) 100%);
  }
  .world-map {
    position: absolute;
    inset: 90px 0 180px 0;
    background: radial-gradient(ellipse at 50% 45%, rgba(120,180,230,0.16), transparent 70%);
  }
  .keyword {
    position: absolute;
    color: var(--word-light);
    text-decoration: underline;
    text-underline-offset: 4px;
    text-decoration-thickness: 1px;
    white-space: nowrap;
  }
  .keyword--major { font-size: 30px; font-weight: 700; }
  .keyword--mid { font-size: 19px; }
  .keyword--minor { font-size: 11px; }
  .keyword--dim { color: var(--word-dim); }

  .contact {
    position: absolute;
    left: 60px; bottom: 70px;
    color: var(--white);
    font-size: 13px;
    line-height: 1.25;
  }
  .contact__brand {
    display: flex; align-items: center; gap: 12px;
    font-size: 20px; font-weight: 500;
    margin-bottom: 16px;
  }
  .contact__square { width: 30px; height: 30px; background: var(--white); }
  .contact__row { display: flex; gap: 10px; align-items: flex-start; margin-bottom: 10px; }
  .contact__row svg { flex: none; width: 16px; height: 16px; }

  .portrait {
    position: absolute;
    left: 30px; top: 190px;
    width: 260px; height: 510px;
    background: linear-gradient(180deg, rgba(240,244,248,0.85) 0%, rgba(220,228,236,0.8) 55%, rgba(20,24,30,0.9) 85%);
    border-radius: 120px 120px 0 0;
  }
  .front-brand {
    position: absolute;
    left: 120px; top: 228px;
    color: var(--white);
    font-size: 52px; font-weight: 500;
    letter-spacing: 0.5px;
  }
  .front-url {
    position: absolute;
    right: 50px; top: 450px;
    color: var(--white);
    font-size: 14px;
  }
  .front-url strong { font-size: 22px; font-weight: 700; }
</style>
</head>
<body>
  <main class="brochure">
    <section class="panel panel--back">
      <div class="world-map" role="img" aria-label="Faint dotted world map in pale blue"></div>
      <span class="keyword keyword--major" style="left:320px; top:78px;">Solution</span>
      <span class="keyword keyword--mid keyword--dim" style="left:275px; top:185px;">Activity</span>
      <span class="keyword keyword--minor keyword--dim" style="left:430px; top:215px;">Web 2.0</span>
      <span class="keyword keyword--minor keyword--dim" style="left:450px; top:270px;">Security</span>
      <span class="keyword keyword--major keyword--dim" style="left:205px; top:285px;">Experience</span>
      <span class="keyword keyword--mid keyword--dim" style="left:340px; top:320px;">Data</span>
      <span class="keyword keyword--mid keyword--dim" style="left:240px; top:380px;">World wide web</span>
      <span class="keyword keyword--major keyword--dim" style="left:315px; top:435px; font-size:26px;">Integration</span>
      <span class="keyword keyword--mid keyword--dim" style="left:205px; top:545px;">communications</span>

      <div class="contact">
        <div class="contact__brand"><span class="contact__square"></span>MallNova</div>
        <div class="contact__row">
          <svg viewBox="0 0 16 16" aria-hidden="true"><path d="M8 1a5 5 0 0 0-5 5c0 4 5 9 5 9s5-5 5-9a5 5 0 0 0-5-5zm0 7a2 2 0 1 1 0-4 2 2 0 0 1 0 4z" fill="#5fc3ee"/></svg>
          <span>Level 2<br>Carrow House<br>15 Venn Street<br>Dalbury SA 5000</span>
        </div>
        <div class="contact__row">
          <svg viewBox="0 0 16 16" aria-hidden="true"><circle cx="8" cy="8" r="8" fill="#5fc3ee"/><path d="M5 4l2 2-1 1a6 6 0 0 0 3 3l1-1 2 2-1 1.5C8 12 4 8 3.5 5z" fill="#fff"/></svg>
          <span>08.5550.1400</span>
        </div>
        <div class="contact__row">
          <svg viewBox="0 0 16 16" aria-hidden="true"><rect x="1" y="3" width="14" height="10" rx="1" fill="#5fc3ee"/><path d="M1 4l7 5 7-5" stroke="#fff" fill="none"/></svg>
          <span>info@mallnova.example</span>
        </div>
      </div>
    </section>

    <section class="panel panel--front">
      <div class="world-map" role="img" aria-label="Faint dotted world map in pale blue"></div>
      <span class="keyword keyword--mid" style="left:120px; top:82px; font-size:15px;">Marketing</span>
      <span class="keyword keyword--major" style="left:290px; top:75px; font-size:22px;">Analyse</span>
      <span class="keyword keyword--minor keyword--dim" style="left:300px; top:305px;">Community</span>
      <span class="keyword keyword--minor keyword--dim" style="left:220px; top:368px;">Investigation</span>
      <span class="keyword keyword--major" style="left:350px; top:335px; font-size:26px;">Grow up</span>
      <div class="portrait" role="img" aria-label="Photo of a businesswoman in a white shirt touching a virtual screen"></div>
      <div class="front-brand">MallNova</div>
      <div class="front-url">www.<strong>MallNova</strong>.example</div>
    </section>
  </main>
</body>
</html>
```